Client Proposal

I need a proposal template to give to potential clients detailing our services, safety, company history, table of contents and appendixes. I need a cover page to start with images describing our services. Our company is based in Grande Prairie, Alberta. We do land survey work, engineering and environmental.

In word format please so that we can change the proposal on an as needed basis.

```html
<!DOCTYPE html>
<html lang="en">
<head>
<meta charset="utf-8">
<title>Northline Group – Project Proposal 2020</title>
<link href="https://fonts.googleapis.com/css2?family=Lato:wght@300;400;700;900&display=swap" rel="stylesheet">
<style>
  :root{
    --blue:#1a9ad6;
    --blue-deep:#1689c2;
    --gray:#8a8b8d;
    --gray-dark:#6b6c6e;
    --ink:#333333;
    --white:#ffffff;
    --stage:#2a2a2a;
    --sky-top:#8fcbe9;
    --sky-bottom:#f2f8fb;
    --land-a:#c9a874;
    --land-b:#9c8a66;
    --warm-a:#e8c9a0;
    --warm-b:#a9714a;
    --print-a:#cfe3f4;
    --print-b:#7aa5d4;
  }
  *{margin:0;padding:0;box-sizing:border-box}
  html,body{width:667px;height:1200px;overflow:hidden;background:var(--stage)}
  body{position:relative;font-family:"Lato",Arial,sans-serif;color:var(--ink)}

  .page{position:absolute;left:189.6px;width:288px;height:373px;overflow:hidden;background:var(--white)}
  .page--cover{top:27px}
  .page--contents{top:414px}
  .page--intro{top:800px}
  .sheet{position:absolute;left:0;top:0;width:618px;height:800px;transform:scale(.4658);transform-origin:0 0}

  /* brand */
  .brand{position:absolute;display:flex;align-items:center;gap:8px;font-weight:900;letter-spacing:.5px;white-space:nowrap}
  .brand__square{width:14px;height:14px;background:currentColor}
  .cover__brand{left:36px;top:100px;font-size:24px;color:var(--blue)}

  /* cover */
  .cover__art{position:absolute;inset:0}
  .cover__title{position:absolute;left:181px;top:196px;line-height:.93}
  .cover__title-main{display:block;font-weight:900;font-size:52px;color:var(--blue)}
  .cover__title-year{display:block;font-weight:400;font-size:52px;color:var(--gray-dark);margin-top:4px}

  /* contents */
  .contents__sky{position:absolute;left:0;top:0;width:618px;height:380px;background:linear-gradient(var(--sky-top),var(--sky-bottom))}
  .contents__land{position:absolute;left:0;top:370px;width:618px;height:430px;background:linear-gradient(#b9c7cf 0%,var(--land-a) 12%,var(--land-b) 100%)}
  .contents__title{position:absolute;left:0;width:618px;top:120px;text-align:center;font-size:19px;font-weight:700;color:var(--ink)}
  .toc{position:absolute;left:146px;top:178px;width:322px;list-style:none;font-size:12px;color:#444}
  .toc li{display:flex;justify-content:space-between;height:22px;line-height:22px}

  /* footer */
  .footer{position:absolute;left:0;top:740px;width:618px;height:34px}
  .footer__art{position:absolute;inset:0}
  .footer__brand{left:48px;top:8px;font-size:14px;color:var(--white)}
  .footer__label{position:absolute;left:418px;top:0;line-height:34px;font-size:13px;font-weight:700}
  .footer__num{position:absolute;left:562px;top:0;line-height:34px;font-size:13px;font-weight:700}
  .footer--blue .footer__label,.footer--blue .footer__num{color:var(--white)}
  .footer--white .footer__label,.footer--white .footer__num{color:var(--gray-dark)}

  /* intro */
  .intro__top{position:absolute;left:0;top:0;width:618px;height:275px;background:var(--white)}
  .intro__band{position:absolute;left:0;top:275px;width:618px;height:525px;background:var(--blue)}
  .intro__title{position:absolute;left:0;width:618px;top:64px;text-align:center;font-size:19px;font-weight:700;color:var(--blue);padding-left:10px}
  .intro__who{position:absolute;left:49px;top:131px;width:530px}
  .intro__who h3{font-size:16px;font-weight:700;color:var(--ink);margin-bottom:4px}
  .intro__who p{font-size:10.6px;line-height:13.4px;color:#444}
  .band__title{position:absolute;left:47px;top:307px;font-size:18px;font-weight:700;color:var(--white);line-height:22px}
  .col{position:absolute;top:385px;width:252px;color:var(--white);font-size:10.6px;line-height:13.4px}
  .col--left{left:49px}
  .col--right{left:323px}
  .col h4{font-size:14px;font-weight:700;line-height:16px;margin-top:12px}
  .col p+p{margin-top:13px}
</style>
</head>
<body>

<!-- Cover -->
<section class="page page--cover">
  <div class="sheet">
    <svg class="cover__art" viewBox="0 0 618 800" aria-hidden="true">
      <defs>
        <linearGradient id="warm" x1="0" y1="0" x2="1" y2="1">
          <stop offset="0" stop-color="var(--warm-a)"/>
          <stop offset="1" stop-color="var(--warm-b)"/>
        </linearGradient>
        <linearGradient id="print" x1="0" y1="0" x2="1" y2="1">
          <stop offset="0" stop-color="var(--print-a)"/>
          <stop offset="1" stop-color="var(--print-b)"/>
        </linearGradient>
      </defs>
      <polygon points="0,290 130,515 0,590" fill="var(--gray)"/>
      <polygon points="130,800 255,728 290,800" fill="var(--gray)"/>
      <polygon points="0,590 130,515 255,728 130,800 0,800" fill="url(#print)"/>
      <polygon points="618,260 618,270 130,515 120,500" fill="#bfe0f1"/>
    </svg>
    <svg class="cover__art" viewBox="0 0 618 800" role="img" aria-label="Photograph of a surveyor with a tripod instrument at a construction site with cranes">
      <polygon points="120,505 570,255 618,262 618,520 255,728" fill="url(#warm)"/>
    </svg>
    <svg class="cover__art" viewBox="0 0 618 800" aria-hidden="true">
      <polygon points="255,728 618,520 618,800 290,800" fill="var(--blue)"/>
      <line x1="300" y1="20" x2="618" y2="170" stroke="#e6e6e6" stroke-width="1.5"/>
      <line x1="240" y1="150" x2="600" y2="800" stroke="var(--white)" stroke-width="1.5"/>
      <line x1="618" y1="630" x2="440" y2="730" stroke="var(--white)" stroke-width="1.5"/>
      <path d="M440,730 Q415,745 418,780 L425,800" fill="none" stroke="var(--white)" stroke-width="1.5"/>
      <path d="M0,420 L20,470 Q30,490 60,480 L120,450" fill="none" stroke="var(--white)" stroke-width="1.5"/>
    </svg>
    <div class="brand cover__brand"><span class="brand__square"></span>NORTHLINE GROUP</div>
    <h1 class="cover__title">
      <span class="cover__title-main">PROJECT</span>
      <span class="cover__title-main">PROPOSAL</span>
      <span class="cover__title-year">2020</span>
    </h1>
  </div>
</section>

<!-- Table of contents -->
<section class="page page--contents">
  <div class="sheet">
    <div class="contents__sky"></div>
    <div class="contents__land" role="img" aria-label="Aerial photograph of a town spreading across dry open land"></div>
    <h2 class="contents__title">TABEL OF CONTENT</h2>
    <ol class="toc">
      <li><span>Table of Contents</span><span>2</span></li>
      <li><span>An Introduction</span><span>3</span></li>
      <li><span>Company History</span><span>4</span></li>
      <li><span>Our Services</span><span>5</span></li>
      <li><span>Safety</span><span>6</span></li>
      <li><span>Appendixes</span><span>7</span></li>
    </ol>
    <footer class="footer footer--blue">
      <svg class="footer__art" viewBox="0 0 618 34" aria-hidden="true">
        <polygon points="0,0 350,0 372,34 0,34" fill="var(--gray)"/>
        <polygon points="372,0 392,0 382,12" fill="var(--gray)"/>
        <polygon points="402,0 618,0 618,34 385,34" fill="var(--blue)"/>
      </svg>
      <div class="brand footer__brand"><span class="brand__square"></span>NORTHLINE GROUP</div>
      <span class="footer__label">PROJECT PROPOSAL</span>
      <span class="footer__num">2</span>
    </footer>
  </div>
</section>

<!-- Introduction -->
<section class="page page--intro">
  <div class="sheet">
    <div class="intro__top"></div>
    <div class="intro__band"></div>
    <h2 class="intro__title">AN INTRODUCTION</h2>
    <div class="intro__who">
      <h3>Who We Are</h3>
      <p>Northline Group is a partnership between Northline Geomatics Inc, in operation since July 2013, and the recently formed Northline Engineering Inc. Northline Geomatics experienced steady growth throughout Alberta since opening for business. The addition of Northline Engineering in January 2016 and led by two senior civil engineers with extensive experience in the Peace Region, makes Northline Group uniquely positioned to offer fully integrated, professional surveying and civil engineering solutions, creating cost effective, innovative outcomes for our clients.</p>
    </div>
    <h2 class="band__title">PROFESSIONALS,<br>PARTNERSHIPS &amp; PROCESS</h2>
    <div class="col col--left">
      <p>At Northline Group Surveying &amp; Engineering, we cultivate a culture that guarantees the best outcomes for your projects every time. This culture starts with a passionate desire to be in partnership with our customers, our colleagues and our communities across Alberta. We aim to offer solutions for any surveying or civil engineering task or project.</p>
      <h4>Our Approach is Partnership &amp; Innovation</h4>
      <p>We work with our clients in consultation and partnership on every project to truly understand your technical needs and expectations (and your budget). Creating successful outcomes with our customers is a fundamental part of our business philosophy and a very rewarding aspect of our work.</p>
      <p>Our professional and technical staff treats every task, from traditional to ‘never been done before’, with best practices and mindset of seeking</p>
    </div>
    <div class="col col--right">
      <p>constant innovation. This means we can use our innovative technology, integrated services and tested processes to deliver exceptional results, beyond your expectations, every time.</p>
      <h4>Commitment to Safety</h4>
      <p>Northline Group has been awarded a Certificate of Recognition (COR) for our safety program. We are devoted to safe work practices and environments for all employees, contractors, subcontractors, clients and the communities where we conduct our business. The well-being of the environment is elemental in our philosophy.</p>
      <h4>Where We Operate</h4>
      <p>We offer a broad scope of Surveying and Civil Engineering services from our offices across Alberta. From the Peace Country to the Southern Foothills and all points in between we offer services to nearly all sectors of industry.</p>
    </div>
    <footer class="footer footer--white">
      <svg class="footer__art" viewBox="0 0 618 34" aria-hidden="true">
        <polygon points="0,0 350,0 372,34 0,34" fill="var(--gray)"/>
        <polygon points="372,0 392,0 382,12" fill="var(--gray)"/>
        <polygon points="402,0 618,0 618,34 385,34" fill="var(--white)"/>
      </svg>
      <div class="brand footer__brand"><span class="brand__square"></span>NORTHLINE GROUP</div>
      <span class="footer__label">PROJECT PROPOSAL</span>
      <span class="footer__num">3</span>
    </footer>
  </div>
</section>

</body>
</html>
```